Book Cover design - Education & Research

We need a design of the book cover for a book written in an education sector. It has been written by a professor with target audience being other professors, lecturers, PhD students etc. The book is about Singapore's development as a country (from third world to economical leader) with high emphasis on it's education sector. It explores many education concepts that could set an example for other countries.
We would like the design to be serious, modern, representing innovation, progress in the educations space. The colours will be mainly red and white representing the country's flag. Probably white background with red additions. The design will consist of three parts:
1) Front cover (the most important where the designer should put most effort in). At the top will be name of the author: Zofia Kradecka, below name of the book: "Odlegle Sciezki Nauczania" with smaller subtitle below: "Zielone Mosty Pomiedzy Szkolami Zielone Mosty Pomiedzy Szkolami"
2) Back cover (very simple with majority of the space put for text, reviews etc.)
3) Second page already inside the book (less important, just a simple black and white design in this part)
We welcome any creative designs from your part, but for reference below is an idea of how we would like it to look like. I would recommend for the designers to do two designs. One according to the below instructions and another with your own idea how to go about it. Please do keep in mind that we can't use proprietary Singapore icons like quorvex or exact design of Singapore flag, so please don't use these.
Our idea:
- The front page to have cityscape with silhouettes of Singapore iconic buildings (Coral Hill Towers, Halvern Wheel, Lumen Craft Gallery, Corvanta, Terraces of Wrenfield, Sky scrappers)
- A red and white ribbon starting at the front and then going through the spine of the book to the back cover.
NOTE:
- We would like to see more designs with your own creativity and other colors, not only red and white
Education sector, Universities, Professors

```html
<!DOCTYPE html>
<html lang="pl">
<head>
<meta charset="utf-8">
<title>Odlegle Sciezki Nauczania – okładka</title>
<link rel="stylesheet" href="https://fonts.googleapis.com/css2?family=Roboto+Condensed:wght@400;700&family=Work+Sans:wght@300;400&display=swap">
<style>
  :root {
    --paper: #ffffff;
    --stage: #ffffff;
    --ink: #111111;
    --ink-soft: #555555;
    --flag-red: #d9131f;
    --flag-red-deep: #b50f1a;
    --steel-light: #dfe3e9;
    --steel: #a9b3c2;
    --steel-dark: #3c5068;
    --shadow: rgba(0,0,0,0.45);
  }
  * { margin: 0; padding: 0; box-sizing: border-box; }
  html, body { width: 1200px; height: 619px; overflow: hidden; background: var(--stage); }
  body { position: relative; font-family: "Work Sans", sans-serif; color: var(--ink); }

  .cover-wrap, .inner-page {
    position: absolute; top: 57px; height: 509px; background: var(--paper);
    box-shadow: 0 0 14px 2px var(--shadow); overflow: hidden;
  }
  .cover-wrap { left: 52px; width: 747px; }
  .inner-page { left: 812px; width: 348px; }

  .artwork { position: absolute; inset: 0; width: 100%; height: 100%; }

  /* back cover */
  .author-portrait {
    position: absolute; left: 28px; top: 47px; width: 124px; height: 156px;
    background: linear-gradient(160deg, #f4f4f4 0%, #1a1a1a 45%, #000 100%);
  }
  .author-bio {
    position: absolute; left: 165px; top: 47px; width: 175px;
    font-size: 8.6px; line-height: 11.35px; font-weight: 400; white-space: nowrap;
  }
  .author-bio .bio-name { font-size: 10.5px; }
  .back-blurb {
    position: absolute; left: 31px; top: 211px; width: 290px;
    font-size: 5.55px; line-height: 7.85px; letter-spacing: 0.15px; white-space: nowrap;
  }

  /* spine */
  .spine-author, .spine-title {
    position: absolute; left: 369px; writing-mode: vertical-rl; white-space: nowrap;
  }
  .spine-author { top: 54px; font-size: 12.5px; font-weight: 400; }
  .spine-title {
    top: 175px; font-family: "Roboto Condensed", sans-serif;
    font-size: 15px; font-weight: 400; letter-spacing: 0.6px; color: var(--flag-red);
  }

  /* front cover */
  .front-author {
    position: absolute; left: 440px; width: 270px; top: 66px; text-align: center;
    font-size: 17px; letter-spacing: 4.2px; font-weight: 400;
  }
  .front-title {
    position: absolute; left: 432px; width: 290px; top: 163px;
    font-family: "Roboto Condensed", sans-serif; white-space: nowrap;
  }
  .front-title h1 { font-size: 21px; font-weight: 700; letter-spacing: 1px; line-height: 22px; color: var(--flag-red); }
  .front-title p { font-size: 9px; font-weight: 700; color: var(--ink); letter-spacing: 0.3px; margin-top: 1px; }

  /* inner title page */
  .inner-author {
    position: absolute; left: 0; width: 100%; top: 63px; text-align: center;
    font-size: 17px; letter-spacing: 4.2px;
  }
  .inner-title {
    position: absolute; left: 0; width: 100%; top: 219px; text-align: center;
    font-family: "Roboto Condensed", sans-serif; white-space: nowrap;
  }
  .inner-title h2 { font-size: 22px; font-weight: 700; letter-spacing: 1.2px; line-height: 24px; }
  .inner-title p { font-size: 15.5px; font-weight: 700; color: var(--ink-soft); letter-spacing: 1px; margin-top: 3px; line-height: 18px; }
</style>
</head>
<body>

<section class="cover-wrap" aria-label="Okładka: tył, grzbiet i przód">
  <svg class="artwork" viewBox="0 0 747 509">
    <defs>
      <linearGradient id="skylineTone" x1="0" y1="0" x2="0" y2="1">
        <stop offset="0" stop-color="#e4e8ee"/>
        <stop offset="0.55" stop-color="#a9b3c2"/>
        <stop offset="1" stop-color="#51657d"/>
      </linearGradient>
      <radialGradient id="rays" cx="1" cy="0.75" r="0.9">
        <stop offset="0" stop-color="#e9eaec"/>
        <stop offset="1" stop-color="#ffffff" stop-opacity="0"/>
      </radialGradient>
    </defs>
    <rect x="440" y="180" width="307" height="250" fill="url(#rays)"/>
    <g class="stars" fill="var(--flag-red)">
      <polygon points="443,211 447,223 460,223 450,231 454,244 443,236 432,244 436,231 426,223 439,223"/>
      <polygon points="466,262 470,273 482,273 472,281 476,293 466,286 456,293 460,281 450,273 462,273"/>
      <polygon points="497,313 501,323 512,323 503,330 506,341 497,334 488,341 491,330 482,323 493,323"/>
      <polygon points="547,353 550,362 560,362 552,368 555,377 547,371 539,377 542,368 534,362 544,362"/>
      <polygon points="597,383 599,389 605,389 600,393 602,399 597,395 592,399 594,393 589,389 595,389"/>
    </g>
    <g role="img" aria-label="Panorama miasta: Coral Hill Towers, Halvern Wheel, Lumen Craft Gallery, Corvanta i Terraces of Wrenfield">
      <rect x="625" y="233" width="122" height="276" rx="60" fill="#eef0f3" opacity="0.6"/>
      <path fill="url(#skylineTone)" opacity="0.9"
        d="M0,360 C30,345 60,330 110,318 C160,312 200,320 230,340 L250,380 L320,400 L380,395 L440,405 L500,395 L560,410 L620,425 L747,430 L747,509 L0,509 Z"/>
    </g>
    <path class="ribbon" fill="var(--flag-red)"
      d="M200,390 C240,360 280,350 320,368 C360,390 400,430 460,428 C520,425 560,408 610,412 C660,418 710,438 747,438 L747,480 C700,485 640,470 590,472 C520,474 470,492 420,490 C340,488 280,450 230,452 C160,455 60,470 0,470 L0,445 C80,440 150,420 200,390 Z"/>
    <path fill="url(#skylineTone)" opacity="0.95" d="M0,470 L120,462 L260,470 L420,488 L560,478 L747,480 L747,509 L0,509 Z"/>
  </svg>

  <div class="author-portrait" role="img" aria-label="Zdjęcie autorki"></div>
  <div class="author-bio">
    <span class="bio-name">Zofia Kradecka</span> about the author<br>
    lorem ipsum lorem ipsum lorem ipsum<br>lorem ipsum lorem ipsum lorem ipsum<br>
    lorem ipsum lorem ipsum lorem ipsum<br>lorem ipsum lorem ipsum lorem ipsum<br>
    lorem ipsum lorem ipsum lorem ipsum<br>lorem ipsum lorem ipsum lorem ipsum<br>
    lorem ipsum lorem ipsum lorem ipsum<br>lorem ipsum lorem ipsum lorem ipsum<br>
    lorem ipsum lorem ipsum lorem ipsum<br>lorem ipsum lorem ipsum lorem ipsum<br>
    lorem ipsum lorem ipsum lorem ipsum<br>lorem ipsum
  </div>
  <div class="back-blurb">
    ODLEGLE SCIEZKI NAUCZANIA, Zielone Mosty Pomiedzy Szkolami Zielone Mosty Pomiedzy Szkolami<br>
    ODLEGLE SCIEZKI NAUCZANIA, Zielone Mosty Pomiedzy Szkolami Zielone Mosty Pomiedzy Szkolami<br>
    ODLEGLE SCIEZKI NAUCZANIA, Zielone Mosty Pomiedzy Szkolami Zielone Mosty Pomiedzy Szkolami<br>
    ODLEGLE SCIEZKI NAUCZANIA, Zielone Mosty Pomiedzy Szkolami Zielone Mosty Pomiedzy Szkolami<br>
    ODLEGLE SCIEZKI NAUCZANIA, Zielone Mosty Pomiedzy Szkolami Zielone Mosty Pomiedzy Szkolami<br>
    ODLEGLE SCIEZKI NAUCZANIA, Zielone Mosty Pomiedzy Szkolami Zielone Mosty Pomiedzy Szkolami<br>
    ODLEGLE SCIEZKI NAUCZANIA, Zielone Mosty Pomiedzy Szkolami Zielone Mosty Pomiedzy Szkolami<br>
    ODLEGLE SCIEZKI NAUCZANIA, Zielone Mosty Pomiedzy Szkolami Zielone Mosty Pomiedzy Szkolami<br>
    ODLEGLE SCIEZKI NAUCZANIA, Zielone Mosty Pomiedzy Szkolami Zielone Mosty Pomiedzy Szkolami<br>
    ODLEGLE SCIEZKI NAUCZANIA, Zielone Mosty Pomiedzy Szkolami Zielone Mosty Pomiedzy Szkolami<br>
    ODLEGLE SCIEZKI NAUCZANIA, Zielone Mosty Pomiedzy Szkolami Zielone Mosty Pomiedzy Szkolami<br>
    ODLEGLE SCIEZKI NAUCZANIA, Zielone Mosty Pomiedzy Szkolami Zielone Mosty Pomiedzy Szkolami
  </div>

  <div class="spine-author">Zofia Kradecka</div>
  <div class="spine-title">ODLEGLE SCIEZKI NAUCZANIA</div>

  <div class="front-author">Zofia Kradecka</div>
  <div class="front-title">
    <h1>ODLEGLE SCIEZKI NAUCZANIA</h1>
    <p>Zielone Mosty Pomiedzy Szkolami Zielone Mosty Pomiedzy Szkolami</p>
  </div>
</section>

<section class="inner-page" aria-label="Strona tytułowa">
  <svg class="artwork" viewBox="0 0 348 509">
    <defs>
      <linearGradient id="innerSkyline" x1="0" y1="0" x2="0" y2="1">
        <stop offset="0" stop-color="#eef0f3"/>
        <stop offset="1" stop-color="#b9c1cc"/>
      </linearGradient>
    </defs>
    <path role="img" aria-label="Szara panorama miasta z kołem widokowym Halvern Wheel"
      fill="url(#innerSkyline)"
      d="M22,430 C40,420 70,415 95,420 L120,440 L170,435 L220,430 L270,440 L275,420 C280,400 300,388 315,388 C330,388 343,400 343,420 L343,509 L22,509 Z"/>
  </svg>
  <div class="inner-author">Zofia Kradecka</div>
  <div class="inner-title">
    <h2>ODLEGLE SCIEZKI NAUCZANIA</h2>
    <p>Zielone Mosty Pomiedzy Szkolami</p>
  </div>
</section>

</body>
</html>
```